Quorvel Landing page redesign

We are looking for a landing page redesign before we officially launch. We want to incorporate the information already on the site at www.Quorvel-example.com landing page but make it more inviting. There needs to be a sign up section along with clearly stating what we do. Having a place for sample profiles and linking to our blog and podcast is option. More information about all we will be doing is at Quorvel is on the landing page and also on the blog.

Target Market(s)

35 years old and up.

Coding

Coded - Design and coding required

Number of Pages Required

1 page

Requirements
Must have
• The top bar and the bottom bar (with the privacy policy, etc)
• Sign in/up section.
• I don't want to give to much here because I want designers to be creative.
Nice to have
• Prefer not to have a landing page that requires a lot of scrolling at all.

```html
<!DOCTYPE html>
<html lang="en">
<head>
<meta charset="utf-8">
<title>Quorvel — Landing</title>
<link href="https://fonts.googleapis.com/css2?family=Roboto:ital,wght@0,400;0,500;0,700;1,400&display=swap" rel="stylesheet">
<style>
:root{
  --navy:#0d2f5e;
  --navy-deep:#0a2548;
  --blue:#1e8fde;
  --blue-bright:#2a9be8;
  --page:#f3f4f6;
  --card:#ebedf0;
  --ink:#222a33;
  --muted:#5d646c;
  --line:#6fb6e8;
  --white:#ffffff;
}
*{box-sizing:border-box;margin:0;padding:0}
html,body{width:764px;height:1200px;overflow:hidden}
body{position:relative;background:var(--page);font-family:"Roboto",sans-serif;color:var(--ink)}
.abs{position:absolute}

/* hero */
.hero{left:0;top:0;width:764px;height:347px;background:linear-gradient(160deg,#7a6a52 0%,#a4794b 35%,#5f5247 65%,#3b3a3e 100%)}
.topbar{left:0;top:0;width:764px;height:43px;border-bottom:1px solid rgba(255,255,255,.35)}
.brand{left:35px;top:12px;display:flex;align-items:center;gap:6px;color:var(--white);font-size:19px;font-weight:500}
.brand-dot{width:9px;height:9px;background:var(--white)}
.nav{left:308px;top:16px;display:flex;gap:0;font-size:10px;font-weight:700;color:var(--white);letter-spacing:.2px}
.nav span{position:absolute;white-space:nowrap}
.btn-pill{top:11px;height:20px;border-radius:10px;font-size:8.5px;font-weight:500;display:flex;align-items:center;justify-content:center}
.btn-login{left:642px;width:39px;border:1.5px solid var(--white);color:var(--white)}
.btn-signup{left:685px;width:49px;background:var(--white);color:var(--ink)}

/* welcome */
.welcome{left:0;top:347px;width:764px;height:71px;background:linear-gradient(90deg,var(--navy-deep) 0%,#114a8a 50%,var(--blue-bright) 100%);color:var(--white);text-align:center}
.welcome h1{position:absolute;left:0;right:0;top:4px;font-size:14px;font-weight:700}
.rule{left:33px;width:698px;border-top:1px dashed var(--line)}
.welcome .rule{border-top-color:rgba(255,255,255,.6);top:27px}
.welcome p{position:absolute;left:33px;right:33px;top:42px;font-size:7.8px;line-height:12.5px}

/* section titles */
.sec-title{left:0;width:764px;text-align:center;font-size:14px;font-weight:700;color:var(--ink)}
.sec-title em{font-style:normal;color:var(--blue)}

/* steps */
.step{width:160px;text-align:center}
.step-circle{position:absolute;width:60px;height:60px;border-radius:50%;background:radial-gradient(circle at 50% 40%,#1b4f8f,var(--navy));box-shadow:0 0 0 2px #dfe6ee}
.step-circle.active{box-shadow:0 0 0 2px var(--white),0 0 0 3px var(--navy)}
.step-circle svg{position:absolute;left:15px;top:15px}
.step-name{font-size:11.5px;font-weight:700;color:var(--ink)}
.step-name.active{color:var(--blue)}
.step-sub{font-size:8px;color:var(--muted)}
.connector{height:1px;background:var(--blue);top:501px}

/* signup */
.signup{left:0;top:598px;width:764px;height:56px;background:linear-gradient(90deg,var(--navy-deep),#1160a8 60%,var(--blue-bright))}
.signup-label{left:72px;top:16px;color:var(--white);font-size:7.8px;font-weight:500;line-height:12px}
.field{top:18px;width:160px;height:20px;background:var(--white);border-radius:2px;font-size:8px;color:#9aa0a6;padding:5px 9px}
.subscribe{left:672px;top:18px;width:75px;height:20px;background:var(--white);border-radius:2px;font-size:8px;font-weight:700;color:var(--ink);display:flex;align-items:center;justify-content:center}

/* blog */
.card{top:710px;width:161px;height:226px;background:var(--card)}
.card-media{width:161px;height:120px}
.card h3{position:absolute;left:12px;top:128px;font-size:11.5px;font-weight:700}
.card p{position:absolute;left:12px;right:10px;top:149px;font-size:7.8px;line-height:12.5px;color:var(--muted)}
.card-rule{position:absolute;left:12px;right:12px;top:196px;border-top:1px dotted #b9bec4}
.card-meta{position:absolute;left:12px;right:12px;top:206px;font-size:7px;color:var(--muted);display:flex;justify-content:space-between;align-items:center}
.card-meta span{display:flex;align-items:center;gap:4px}

/* testimonials */
.quote{top:1017px;width:258px;font-size:8px;font-style:italic;line-height:12.5px;color:var(--muted)}
.quote-left{left:36px;text-align:right}
.quote-right{left:470px}
.quote-name{font-style:normal;color:var(--ink);font-weight:500;margin-top:6px;font-size:8px}
.avatar{width:49px;height:49px;border-radius:50%;background:linear-gradient(160deg,#d9d2c8,#9e8a78)}
.divider-v{left:382px;top:1018px;height:50px;border-left:1px dashed #9aa3ad}
.skyline{top:1072px;height:46px;background:linear-gradient(180deg,rgba(30,143,222,.15),var(--blue-bright))}
.baseline{left:0;top:1116px;width:764px;height:2px;background:var(--blue)}

/* footer */
.footer{left:0;top:1118px;width:764px;height:82px;background:var(--page)}
.foot-main{left:60px;top:33px;display:flex;gap:17px;font-size:8px;font-weight:700;color:var(--ink)}
.foot-rule{left:38px;width:688px;top:51px;border-top:1px solid #d3d7dc}
.foot-sub{left:39px;top:60px;display:flex;gap:13px;font-size:7px;color:var(--ink)}
.foot-right{right:38px;top:60px;display:flex;gap:13px;font-size:7px;color:var(--ink)}
.foot-brand{right:38px;top:23px;font-size:14px;font-weight:500;color:var(--ink);display:flex;align-items:center;gap:6px}
.foot-brand .brand-dot{background:var(--ink);width:8px;height:8px}
</style>
</head>
<body>

<div class="abs hero" role="img" aria-label="Photo of friends laughing on a rooftop under a shower of confetti at sunset"></div>
<header class="abs topbar">
  <div class="abs brand"><span class="brand-dot"></span>Quorvel</div>
  <nav class="abs nav" style="left:0;top:16px">
    <span style="left:308px">HOME</span>
    <span style="left:362px">BLOG</span>
    <span style="left:410px">PODCAST</span>
  </nav>
  <div class="abs btn-pill btn-login">Log In</div>
  <div class="abs btn-pill btn-signup">Sign Up</div>
</header>

<section class="abs welcome">
  <h1>Welcome to Quorvel</h1>
  <div class="abs rule"></div>
  <p>Sed ut perspiciatis unde omnis iste natus error sit voluptatem accusantium doloremque laudantium, totam rem aperiam, eaque ipsa quae ab illo inventore veritatis et quasi architecto beatae vitae dicta sunt explicabo.</p>
</section>

<h2 class="abs sec-title" style="top:421px">How it <em>Works</em></h2>
<div class="abs rule" style="top:446px"></div>

<div class="abs connector" style="left:155px;width:96px"></div>
<div class="abs connector" style="left:334px;width:96px"></div>
<div class="abs connector" style="left:513px;width:96px"></div>

<div class="step-circle" style="left:84px;top:471px">
  <svg width="30" height="30" viewBox="0 0 30 30" fill="none" stroke="#fff" stroke-width="1.6"><rect x="3" y="4" width="24" height="22"/><line x1="3" y1="10" x2="27" y2="10"/><rect x="7" y="14" width="7" height="8"/><line x1="17" y1="15" x2="24" y2="15"/><line x1="17" y1="19" x2="24" y2="19"/><line x1="17" y1="23" x2="24" y2="23"/></svg>
</div>
<div class="step-circle" style="left:262px;top:471px">
  <svg width="30" height="30" viewBox="0 0 30 30"><rect x="3" y="5" width="24" height="20" fill="none" stroke="#fff" stroke-width="2"/><path d="M15 21 L9 15 A3 3 0 0 1 15 11 A3 3 0 0 1 21 15 Z" fill="#fff"/></svg>
</div>
<div class="step-circle active" style="left:441px;top:471px">
  <svg width="30" height="30" viewBox="0 0 30 30" fill="none" stroke="#fff" stroke-width="1.6"><circle cx="15" cy="7" r="3" fill="#fff"/><path d="M15 11v10M15 21l-6 5M15 21l6 5M6 13l-3 4M24 13l3 4M5 22a12 12 0 0 0 20 0"/></svg>
</div>
<div class="step-circle" style="left:618px;top:471px">
  <svg width="30" height="30" viewBox="0 0 30 30"><path d="M10 13V9a5 5 0 0 1 10 0" fill="none" stroke="#fff" stroke-width="2.5"/><rect x="8" y="13" width="14" height="13" rx="1.5" fill="#fff"/><circle cx="15" cy="19" r="2" fill="#0d2f5e"/></svg>
</div>

<div class="abs step" style="left:34px;top:545px"><div class="step-name">Create</div><div class="step-sub" style="margin-top:6px">Timelines, Maps, Family Trees</div></div>
<div class="abs step" style="left:212px;top:545px"><div class="step-name">Memorialize</div><div class="step-sub" style="margin-top:6px">Loved Ones</div></div>
<div class="abs step" style="left:391px;top:545px"><div class="step-name active">Share</div><div class="step-sub" style="margin-top:6px">Family Stories, History and more</div></div>
<div class="abs step" style="left:568px;top:545px"><div class="step-name">Control</div><div class="step-sub" style="margin-top:6px">Your Privacy</div></div>

<section class="abs signup">
  <svg class="abs" style="left:32px;top:17px" width="24" height="22" viewBox="0 0 24 22" fill="#fff"><circle cx="12" cy="5" r="4"/><circle cx="4.5" cy="8" r="3"/><circle cx="19.5" cy="8" r="3"/><path d="M5 22v-6a7 7 0 0 1 14 0v6z"/><path d="M0 20v-4a4.5 4.5 0 0 1 6-4v8zM24 20v-4a4.5 4.5 0 0 0-6-4v8z"/></svg>
  <div class="abs signup-label">Create a New<br>Account</div>
  <div class="abs field" style="left:153px">Full Name *</div>
  <div class="abs field" style="left:326px">Your Email *</div>
  <div class="abs field" style="left:499px">Password *</div>
  <div class="abs subscribe">SUBSCRIBE</div>
</section>

<h2 class="abs sec-title" style="top:660px">Latest <em>Blog &amp; Views</em></h2>
<div class="abs rule" style="top:685px"></div>

<article class="abs card" style="left:33px">
  <div class="card-media" role="img" aria-label="Photo of a traveller with a leather backpack walking out of a doorway" style="background:linear-gradient(135deg,#e8e4de,#6b4a34)"></div>
  <h3>Standard Post</h3>
  <p>Enim congue blandit. Lorem ipsum dolor sit amet, consectetur adipiscing elit. Quisque...</p>
  <div class="card-rule"></div>
  <div class="card-meta"><span>&#9638; 22 June, 2015</span><span>&#9679; 0</span></div>
</article>
<article class="abs card" style="left:212px">
  <div class="card-media" role="img" aria-label="Photo of a glass coffee carafe on a table beside a plant" style="background:linear-gradient(135deg,#c9ccc8,#5e5a52)"></div>
  <h3>Video Post</h3>
  <p>Ultrices posuere cubilia curae curabitur sit amet tortor ut massa commodo. Vestibulum...</p>
  <div class="card-rule"></div>
  <div class="card-meta"><span>&#9638; 22 June, 2015</span><span>&#9679; 0</span></div>
</article>
<article class="abs card" style="left:391px">
  <div class="card-media" role="img" aria-label="Photo of a café table and white chair against a brick wall" style="background:linear-gradient(135deg,#6d4f3e,#b39a82)"></div>
  <h3>Post with Image</h3>
  <p>Enim congue blandit. Lorem ipsum dolor sit amet, consectetur adipiscing elit. Quisque...</p>
  <div class="card-rule"></div>
  <div class="card-meta"><span>&#9638; 22 June, 2015</span><span>&#9679; 0</span></div>
</article>
<article class="abs card" style="left:570px">
  <div class="card-media" role="img" aria-label="Photo of an old leather wallet in front of a butterfly display" style="background:linear-gradient(135deg,#d8cfc3,#7c5a42)"></div>
  <h3>Image Post</h3>
  <p>Ultrices posuere cubilia curae curabitur sit amet tortor ut massa commodo. Vestibulum...</p>
  <div class="card-rule"></div>
  <div class="card-meta"><span>&#9638; 22 June, 2015</span><span>&#9679; 3</span></div>
</article>

<h2 class="abs sec-title" style="top:962px">What <em>People Say</em></h2>
<div class="abs rule" style="top:988px"></div>

<blockquote class="abs quote quote-left">Duis aute irure dolor in reprehenderit in voluptate velit esse cillum dolore eu fugiat nulla pariatur. Excepteur sint occaecat cupidatat non proident, sunt in culpa qui officia deserunt mollit.<div class="quote-name">Marek Holt, Operations Manager</div></blockquote>
<div class="abs avatar" style="left:312px;top:1017px" role="img" aria-label="Portrait photo of Marek Holt"></div>
<div class="abs divider-v"></div>
<div class="abs avatar" style="left:403px;top:1017px" role="img" aria-label="Portrait photo of Tessa Morlan"></div>
<blockquote class="abs quote quote-right">Provident, similique sunt in culpa qui officia deserunt mollitia animi, id est laborum et dolorum fuga. Et harum quidem rerum facilis est et expedita distinctio. Nam libero tempore, cum soluta nobis.<div class="quote-name">Tessa Morlan, Creative Designer</div></blockquote>

<div class="abs skyline" style="left:0;width:198px" role="img" aria-label="Blue city skyline silhouette"></div>
<div class="abs skyline" style="left:466px;width:298px" role="img" aria-label="Blue airport silhouette with control tower and planes"></div>
<div class="abs baseline"></div>

<footer class="abs footer">
  <svg class="abs" style="left:39px;top:33px" width="9" height="9" viewBox="0 0 9 9" fill="none" stroke="#222a33" stroke-width="1.4"><circle cx="3.6" cy="3.6" r="2.8"/><line x1="5.6" y1="5.6" x2="8.5" y2="8.5"/></svg>
  <nav class="abs foot-main"><span>Help &amp; Contact</span><span>Fees</span><span>Security</span><span>Podcast</span></nav>
  <div class="abs foot-brand"><span class="brand-dot"></span>Quorvel</div>
  <div class="abs foot-rule"></div>
  <nav class="abs foot-sub"><span>About</span><span>Blog</span><span>Jobs</span><span>Data Tracking Policy</span><span>Public Policy</span><span>Sitemap</span><span>Partners</span></nav>
  <div class="abs foot-right"><span>&copy; 2015–2017</span><span>Terms of Use</span><span>Feedback</span></div>
</footer>

</body>
</html>
```